Varlow Business Partners
Business Cards & Stationery
Professional
Thomas E. Varlow
CEO
58 Birch Lane, North
Suite 318
Edgeton, NJ 07415
thomas.varlow@varlowbp.com
Back of card should contain the black version of the logo - no other information

```html
<!DOCTYPE html>
<html lang="en">
<head>
<meta charset="utf-8">
<title>Varlow Business Partners – Business Card</title>
<link rel="stylesheet" href="https://fonts.googleapis.com/css2?family=PT+Sans:wght@400;700&display=swap">
<style>
  :root {
    --backdrop: #e4e4e4;
    --card: #ffffff;
    --orange: #f26f21;
    --orange-dark: #d95d12;
    --swoosh: #b4b5b8;
    --ink: #1c1c1c;
    --text-grey: #58595b;
    --brand-grey: #6d6e71;
    --divider: #c9cacc;
  }
  * { box-sizing: border-box; margin: 0; padding: 0; }
  html, body {
    width: 1200px; height: 780px; overflow: hidden;
    background: var(--backdrop);
    font-family: "PT Sans", Arial, sans-serif;
  }
  .canvas {
    position: relative; width: 1200px; height: 780px;
  }
  .business-card {
    position: absolute; left: 100px; top: 90px;
    width: 1000px; height: 600px;
    background: var(--card);
    border-radius: 36px;
    overflow: hidden;
    box-shadow: 0 10px 30px rgba(0,0,0,.18);
  }
  .card-bands { position: absolute; inset: 0; }
  .holder {
    position: absolute; right: 52px; top: 42px; text-align: right; color: var(--ink);
  }
  .holder-name { font-size: 40px; font-weight: 700; line-height: 1.1; }
  .holder-title { font-size: 22px; margin-top: 4px; }
  .brand {
    position: absolute; left: 62px; top: 388px;
    display: flex; align-items: center; gap: 16px;
  }
  .brand-dot {
    width: 26px; height: 26px; border-radius: 50%; background: var(--orange);
  }
  .brand-name {
    font-size: 33px; font-weight: 700; color: var(--brand-grey); letter-spacing: .3px;
  }
  .divider {
    position: absolute; left: 500px; top: 265px; width: 2px; height: 245px;
    background: var(--divider);
  }
  .contact {
    position: absolute; left: 530px; top: 272px; color: var(--text-grey);
    font-size: 24px; line-height: 1.32;
  }
  .contact-lines { margin-top: 34px; }
  .contact-row { display: flex; align-items: center; gap: 14px; margin-bottom: 8px; }
  .contact-icon { width: 22px; height: 22px; flex: none; }
</style>
</head>
<body>
<div class="canvas">
  <article class="business-card">
    <svg class="card-bands" viewBox="0 0 1000 600" width="1000" height="600" aria-hidden="true">
      <path d="M0 0 H1000 V150 C760 158 470 178 260 218 C160 237 70 262 0 290 Z" fill="var(--orange)"/>
      <path d="M300 212 C520 170 780 160 1000 156 V188 C800 188 560 198 300 212 Z" fill="var(--swoosh)"/>
    </svg>

    <header class="holder">
      <p class="holder-name">Thomas E. Varlow</p>
      <p class="holder-title">CEO</p>
    </header>

    <div class="brand">
      <span class="brand-dot"></span>
      <span class="brand-name">Varlow Business Partners</span>
    </div>

    <div class="divider"></div>

    <address class="contact" style="font-style:normal">
      <p>58 Birch Lane, North<br>Suite 318,<br>Edgeton, NJ 07415</p>
      <div class="contact-lines">
        <p class="contact-row">
          <svg class="contact-icon" viewBox="0 0 24 24" aria-hidden="true">
            <path d="M6.6 10.8c1.4 2.8 3.8 5.1 6.6 6.6l2.2-2.2c.3-.3.7-.4 1-.2 1.1.4 2.3.6 3.6.6.6 0 1 .4 1 1V20c0 .6-.4 1-1 1C10.6 21 3 13.4 3 4c0-.6.4-1 1-1h3.5c.6 0 1 .4 1 1 0 1.3.2 2.5.6 3.6.1.3 0 .7-.2 1z" fill="var(--orange)"/>
          </svg>
          555.204.3816
        </p>
        <p class="contact-row">
          <svg class="contact-icon" viewBox="0 0 24 24" aria-hidden="true">
            <rect x="2" y="5" width="20" height="14" rx="2" fill="var(--orange)"/>
            <path d="M3 6.5 L12 13 L21 6.5" fill="none" stroke="#fff" stroke-width="1.8"/>
          </svg>
          thomas.varlow@varlowbp.com
        </p>
      </div>
    </address>
  </article>
</div>
</body>
</html>
```